Two (Similar) Posters - Both 11" x 17"

We are looking for two posters - both 11" x 17" (vertical orientation) - to promote two consecutive, cardiology-related events:

Poster #1) The Inaugural New York RMC Quizline Competition, Cocktail Reception and Whiskey Tasting (http://brelvan-hsq.org/quizline-and-reception)

and

Poster #2) The 89th Annual Scientific Session and 27th Annual Meeting (http://brelvan-hsq.org/2017annualmtg)

#1 is a cocktail party with a whiskey tasting that will also feature a gameshow-like event with the med students, and #2 is an educational conference for doctors

Target Market(s)

Healthcare providers (Please do not include stock images of medical professionals; in fact, please use caution with any stock imagery, as it most likely will not be appropriate.)

Industry/Entity Type

Education

Colors

Designer to choose colors to be used in the design.

Requirements
Must have
• Each poster design should include:
• - the 4 logos of the participating organizations (I can upload various other versions if needed) along with the "wording" that goes alongside each one (see "STD_small" image as an example)
• - name of event
• - date, time and location
• - where to register
• - where to get more information
• - some artistic flavor or detailing
• Final (raw) files in an .ai, .psd, .eps or .idml format are required upon project completion.
Nice to have
• It's not crucial that these two posters "match," but it would be nice if they at least coordinated with each other. Would be nice if the designer could stay close to our color scheme (can be found here - http://brelvan-hsq.org/), but this isn't crucial. Posters should be upscale, neat and professional.
Should not have
• Should not be too difficult to read. These are posters that will likely be hanging on a bulletin board in hospital staff break rooms. Should not be too cartoon-like or silly. The two should not look EXACTLY the same in case people think that they are the same poster.

```html
<!DOCTYPE html>
<html lang="en">
<head>
<meta charset="utf-8">
<title>New York RMC Quizline Competition</title>
<link rel="stylesheet" href="https://fonts.googleapis.com/css2?family=Fira+Sans:ital,wght@0,300;0,400;0,500;0,700;1,400&display=swap">
<style>
:root{
  --navy:#151c4c;
  --navy-deep:#0c1238;
  --navy-band:#1a2156;
  --gold:#d5b264;
  --white:#ffffff;
  --footer-grey:#ececee;
  --ink:#2a2d45;
}
*{box-sizing:border-box;margin:0;padding:0}
html,body{width:870px;height:1200px;overflow:hidden;background:var(--white)}
body{font-family:"Fira Sans",sans-serif;position:relative}
.poster{position:absolute;inset:0;width:870px;height:1200px}
.hero{position:absolute;left:35px;top:35px;width:800px;height:937px;overflow:hidden;
  background:var(--navy)}
.hero-scene{position:absolute;inset:0;
  background:
    radial-gradient(ellipse 260px 420px at 640px 520px,rgba(70,90,170,.35),transparent 70%),
    radial-gradient(ellipse 90px 90px at 505px 325px,rgba(120,140,210,.35),transparent 70%),
    radial-gradient(ellipse 300px 300px at 30px 360px,rgba(70,85,160,.3),transparent 70%),
    linear-gradient(180deg,#1b2358 0%,#182052 45%,#111843 100%)}
.corner-frame{position:absolute;left:0;top:0;width:800px;height:400px}
.corner-ornament{position:absolute;left:645px;top:48px;width:105px;height:115px;
  background:radial-gradient(circle at 70% 30%,rgba(255,255,255,.35),rgba(255,255,255,.08) 70%);
  border-radius:0 0 0 90px}
.copy{position:absolute;left:87px;top:0;width:620px;color:var(--white)}
.eyebrow,.title,.subtitle{color:var(--gold);font-weight:700;text-transform:uppercase;letter-spacing:.2px;position:absolute;left:0;white-space:nowrap}
.eyebrow{top:100px;font-size:37px}
.title{top:150px;font-size:63px;line-height:1}
.subtitle{top:230px;font-size:37px}
.divider{position:absolute;left:-5px;width:390px;height:24px}
.divider-top{top:300px}
.divider-bottom{top:442px}
.event-kind{position:absolute;top:340px;font-size:37px;font-weight:400;line-height:1.2}
.date{position:absolute;top:515px;font-size:25px;line-height:33px}
.date strong{font-weight:700}
.venue{position:absolute;top:610px;font-size:20px;line-height:30px}
.price{position:absolute;top:698px;font-size:15px;line-height:22px}
.register{position:absolute;top:780px;display:flex;height:26px;font-size:19px;line-height:24px}
.register-label{border:1px solid var(--white);padding:0 6px;color:var(--white)}
.register-link{background:var(--gold);color:var(--navy-deep);padding:0 6px;font-weight:500}
.info{position:absolute;top:838px;font-size:20px;line-height:28px;white-space:nowrap}
.info strong{font-weight:700}
.partners{position:absolute;left:35px;top:972px;width:800px;height:133px;background:var(--footer-grey);
  display:flex;align-items:center;padding-left:48px}
.partner{display:flex;align-items:center;margin-right:34px}
.partner-mark{width:96px;height:96px;border-radius:50%;background:var(--white);border:2px solid #9ea1b3;flex:none}
.partner-mark.square{border-radius:0;width:62px;height:72px;border-color:#b4b6c4}
.partner-name{margin-left:12px;font-size:10.5px;line-height:13px;font-style:italic;color:var(--ink);width:140px}
.base-band{position:absolute;left:35px;top:1105px;width:800px;height:60px;background:var(--navy-band)}
</style>
</head>
<body>
<main class="poster">
  <section class="hero">
    <div class="hero-scene" role="img" aria-label="Dimly lit whiskey bar interior with set tables and backlit bottle shelves, tinted deep blue"></div>
    <svg class="corner-frame" viewBox="0 0 800 400" aria-hidden="true">
      <line x1="480" y1="52" x2="753" y2="52" stroke="#ffffff" stroke-width="1.2"/>
      <line x1="753" y1="52" x2="753" y2="330" stroke="#ffffff" stroke-width="1.2"/>
      <rect x="747" y="255" width="12" height="40" fill="#ffffff" opacity=".35"/>
    </svg>
    <div class="corner-ornament" role="img" aria-label="White lace filigree corner ornament"></div>
    <div class="copy">
      <p class="eyebrow">The Inaugural</p>
      <h1 class="title">New York RMC</h1>
      <p class="subtitle">Quizline Competition</p>
      <svg class="divider divider-top" viewBox="0 0 390 24" aria-hidden="true">
        <defs><linearGradient id="rule" x1="0" x2="1"><stop offset="0" stop-color="#d5b264" stop-opacity="0"/><stop offset=".4" stop-color="#d5b264"/><stop offset="1" stop-color="#d5b264" stop-opacity="0"/></linearGradient></defs>
        <line x1="0" y1="12" x2="390" y2="12" stroke="url(#rule)" stroke-width="1.4"/>
        <rect x="165" y="6" width="60" height="12" rx="6" fill="#d5b264" role="img" aria-label="Gold scroll flourish"/>
      </svg>
      <h2 class="event-kind">Cocktail Reception &amp;<br>Whiskey Tasting</h2>
      <svg class="divider divider-bottom" viewBox="0 0 390 24" aria-hidden="true">
        <line x1="0" y1="12" x2="390" y2="12" stroke="url(#rule)" stroke-width="1.4"/>
        <rect x="165" y="6" width="60" height="12" rx="6" fill="#d5b264" role="img" aria-label="Gold scroll flourish"/>
      </svg>
      <p class="date"><strong>Wednesday, Dec. 6th, 2017</strong><br>from 6:30 p.m. to 10:30 p.m.</p>
      <p class="venue">Oak &amp; Ember, 14 Harlow Ln,<br>New York, NY 10099</p>
      <p class="price">Free for BHSQ/HSQ Members and<br>$30 for nonmembers and guests</p>
      <p class="register"><span class="register-label">Register online at</span><span class="register-link">brelvan-hsq.org/2017annualmtg</span></p>
      <p class="info">For more information or to inquire about becoming an exhibitor,<br><strong>call (555) 014-0228</strong> or <strong>email ask@brelvan-hsq.org</strong></p>
    </div>
  </section>
  <footer class="partners">
    <div class="partner"><span class="partner-mark"></span><p class="partner-name">Presented by<br>The Brelvan Heart<br>Society, Inc.</p></div>
    <div class="partner"><span class="partner-mark"></span><p class="partner-name">of the<br>Brelvan State Chapter,<br>Harbor College of Cardiology</p></div>
    <div class="partner"><span class="partner-mark square"></span><p class="partner-name">In Association with<br>Brelvan Cardiac Center</p></div>
  </footer>
  <div class="base-band"></div>
</main>
</body>
</html>
```